LANDCAPE Business Card Design

We need a business card design close to what we are sending you, just more professional. We are a landscape management company located on Topsail Island so an island theme would be great. We would like to stay with a black background and bright green lettering. Something to stand out.

Target Market(s)

Commercial and private property owners

Industry/Entity Type

Landscape

Contact Information for Business Card

BRACKENFORD GROUNDS CARE, LLC,CULTIVATE YOUR OWN ISLAND HAVEN, WADE PELLIN 336-555-0184, MILES DORAHT 910-555-0137

Font styles to use
Sans Serif

```html
<!DOCTYPE html>
<html lang="en">
<head>
<meta charset="utf-8">
<title>Brackenford Grounds Care – Business Card</title>
<link rel="stylesheet" href="https://fonts.googleapis.com/css2?family=Arimo:wght@400;700&family=Archivo:wght@800&display=swap">
<style>
  :root {
    --page-bg: #f2f2f2;
    --card-black: #0b0b0b;
    --card-edge: #1c1c1c;
    --brand-green: #1fd35a;
    --band-green: #1cc04f;
    --band-text: #0a1a0e;
    --contact-white: #f4f4f4;
  }
  * { margin: 0; padding: 0; box-sizing: border-box; }
  html, body {
    width: 1200px;
    height: 900px;
    overflow: hidden;
    background: var(--page-bg);
  }
  .canvas {
    position: relative;
    width: 1200px;
    height: 900px;
  }
  .business-card {
    position: absolute;
    left: 150px;
    top: 193px;
    width: 900px;
    height: 514px;
    border-radius: 42px;
    background: radial-gradient(ellipse at 50% 35%, #2a2a2a 0%, var(--card-black) 70%);
    border: 2px solid var(--card-edge);
    overflow: hidden;
    font-family: "Arimo", Arial, sans-serif;
  }
  .brand-name {
    position: absolute;
    left: 0;
    right: 0;
    top: 72px;
    text-align: center;
    color: var(--brand-green);
    font-weight: 400;
    line-height: 1;
  }
  .brand-name .brand-main {
    display: block;
    font-size: 74px;
    letter-spacing: 2px;
  }
  .brand-name .brand-sub {
    display: block;
    margin-top: 12px;
    font-size: 34px;
    letter-spacing: 5px;
  }
  .tagline-band {
    position: absolute;
    left: 0;
    right: 0;
    top: 232px;
    height: 34px;
    background: var(--band-green);
    display: flex;
    align-items: center;
    justify-content: center;
  }
  .tagline {
    font-family: "Archivo", "Arial Black", sans-serif;
    font-weight: 800;
    font-size: 22px;
    letter-spacing: 7px;
    color: var(--band-text);
    text-transform: uppercase;
    white-space: nowrap;
  }
  .contact {
    position: absolute;
    line-height: 1.25;
  }
  .contact .contact-name {
    display: block;
    color: var(--brand-green);
    font-size: 27px;
    letter-spacing: 0.5px;
  }
  .contact .contact-phone {
    display: block;
    color: var(--contact-white);
    font-size: 30px;
  }
  .contact--left { left: 36px; top: 322px; }
  .contact--right { right: 60px; top: 288px; text-align: left; }
</style>
</head>
<body>
  <main class="canvas">
    <section class="business-card" aria-label="Business card">
      <h1 class="brand-name">
        <span class="brand-main">BRACKENFORD</span>
        <span class="brand-sub">GROUNDS CARE, LLC</span>
      </h1>
      <div class="tagline-band">
        <p class="tagline">Cultivate Your Own Island Haven</p>
      </div>
      <div class="contact contact--left">
        <span class="contact-name">WADE PELLIN</span>
        <span class="contact-phone">336-555-0184</span>
      </div>
      <div class="contact contact--right">
        <span class="contact-name">MILES DORAHT</span>
        <span class="contact-phone">910-555-0137</span>
      </div>
    </section>
  </main>
</body>
</html>
```